Web Design Project for velbrook

We are looking for a sleek and sophisticated website design for our already developed web-based gallery management software application. Here is a link to our web-app: http://www.vel-brook.co

You will login on the main page and then we would like to include all of the information on the PDF that I am providing below (it outlines what?, where?, why? who? and how much?). Basically, we need a home page, about page, and a pricing page, as well as a sign up page that should be navigable from the upper right hand corner of the site where the sign in/sign up would be located. Also, our 3 tenets are that the software program is "attractive, accessible, and affordable", which might need to be somehow incorporated. There are a few websites that we would like for you to take inspiration from listed below:

https://tidemoxen.com (for homepage)
https://plumwovenly.com (for homepage/pricing page/etc)
https://tidemoxen.com/tour (for a tour of how the product works)

We are currently having a logo designed and will share that as soon as it is available! Also, let us know if you need photos/screen shots, as we can provide them.

Thanks!

Reason: Extending deadline as we are just now getting designs we would like to see fully developed.

Target Market(s)

art galleries, artists, art collectors, art consultants, museums

Industry/Entity Type

Software

Requirements
Must have
• Home page
About page (or tour through the app)
Pricing page
Sign up page (the more click-throughs to signing up the better)

```html
<!DOCTYPE html>
<html lang="en">
<head>
<meta charset="utf-8">
<title>velbrook — Gallery Management Software</title>
<link rel="stylesheet" href="https://fonts.googleapis.com/css2?family=Arimo:wght@400;700&display=swap">
<style>
:root{
  --blue:#0a84c6;
  --blue-dark:#0670aa;
  --ink:#333333;
  --text:#8a8a8a;
  --nav:#3a3a3a;
  --band:#f3f3f3;
  --white:#ffffff;
  --rule:#e2e2e2;
}
*{margin:0;padding:0;box-sizing:border-box}
html,body{width:1200px;height:2683px;overflow:hidden;background:var(--white)}
body{font-family:"Arimo",Arial,sans-serif;color:var(--text)}
.page{position:relative;width:1200px;height:2683px;overflow:hidden}
.section{position:absolute;left:0;width:1200px}
.abs{position:absolute}
a{color:inherit;text-decoration:none}

/* header */
.site-header{top:0;height:133px;background:linear-gradient(#ffffff,#e9e9e9)}
.brand{left:129px;top:56px;font-size:40px;color:var(--blue);letter-spacing:-.5px}
.main-nav{left:540px;top:70px;display:flex;font-size:18px;color:var(--nav)}
.main-nav a{padding:0 14px;border-left:1px solid var(--nav);line-height:16px}
.main-nav a:first-child{border-left:0;padding-left:0}
.btn{display:block;background:var(--blue);color:var(--white);font-size:15px;text-align:center;line-height:36px;height:36px}
.header-cta{left:971px;top:66px;width:120px}

/* hero */
.hero{top:133px;height:491px;background:linear-gradient(90deg,#d8573b 0%,#e7c64a 8%,#3a8fc8 16%,#cfcbc6 26%,#c9c4be 60%,#b9a08c 78%,#9aa9b7 100%)}
.hero-dots{left:574px;top:448px;display:flex;gap:4px}
.hero-dots span{width:11px;height:11px;border-radius:50%;background:#1d1d1d}
.hero-dots span:first-child{background:var(--white);border:2px solid #1d1d1d}

/* feature blocks */
.band{background:var(--band)}
.feature-title{font-size:43px;color:var(--ink);font-weight:400}
.feature-copy{font-size:15px;line-height:25.5px;text-align:justify;hyphens:auto;-webkit-hyphens:auto}
.feature-btn{width:121px}

.what{top:624px;height:367px}
.what .shot{left:139px;top:81px;width:380px;height:216px;background:linear-gradient(#fbfbfb,#e8ecef);box-shadow:0 4px 12px rgba(0,0,0,.35)}
.what .feature-title{left:536px;top:66px}
.what .feature-copy{left:542px;top:128px;width:527px}
.what .feature-btn{left:950px;top:289px}

.where{top:991px;height:387px}
.where .feature-title{left:130px;top:45px}
.where .feature-copy{left:130px;top:108px;width:532px}
.where .feature-btn{left:549px;top:254px;width:120px}
.where .photo{left:751px;top:0;width:449px;height:387px;background:linear-gradient(90deg,#ffffff 0%,#e9ddd4 35%,#7a5a45 60%,#2f5f8e 85%,#c9762f 100%)}

.why{top:1378px;height:369px}
.why .feature-title{left:535px;top:28px}
.why .art{left:170px;top:115px;width:313px;height:126px;background:radial-gradient(ellipse at center,#9a9a9a 0%,#d6d6d6 55%,var(--band) 80%)}
.why .feature-copy{left:531px;top:104px;width:529px}
.why .feature-btn{left:939px;top:296px}

.price{top:1747px;height:369px}
.price .feature-title{left:132px;top:78px}
.price .price-body{left:132px;top:145px;width:530px}
.price .signup-line{margin-top:18px;font-size:29px;color:#666}
.price .signup-line a{color:var(--blue)}
.price .device{left:751px;top:50px;width:263px;height:319px;background:linear-gradient(#2a2a2a,#474747 40%,#6b5a3c 70%,#1f2f4e);border-radius:16px 16px 0 0}

/* newsletter */
.newsletter{top:2116px;height:277px;text-align:center}
.newsletter h2{position:absolute;left:0;width:1200px;top:63px;font-size:32px;font-weight:400;color:var(--blue)}
.newsletter p{position:absolute;left:0;width:1200px;top:107px;font-size:14.5px;color:var(--ink)}
.email-field{left:245px;top:140px;width:710px;height:43px;background:var(--white);border:1px solid #eaeaea}
.subscribe{left:513px;top:201px;width:149px;height:45px;line-height:45px;background:linear-gradient(#1b93d2,var(--blue-dark));color:var(--white);font-size:21px;border-radius:4px;box-shadow:0 2px 3px rgba(0,0,0,.3)}

/* footer */
.site-footer{top:2393px;height:243px}
.footer-about{left:130px;top:20px;width:383px}
.footer-about h3{font-size:18px;font-weight:400;color:var(--blue);margin-bottom:2px}
.footer-about p{font-size:14px;line-height:24px;text-align:justify;hyphens:auto;-webkit-hyphens:auto}
.footer-links{top:27px;list-style:none;font-size:13px;line-height:33.5px}
.links-a{left:529px}
.links-b{left:690px}
.social{left:930px;top:24px;list-style:none;font-size:13px;color:var(--ink)}
.social li{position:relative;height:38px;line-height:30px;width:110px}
.social li span{position:absolute;left:70px;top:2px;width:28px;height:28px;border-radius:50%;background:var(--blue)}

.legal{top:2636px;height:47px;border-top:1px solid var(--rule);text-align:center;font-size:13px;line-height:46px;color:#555}
</style>
</head>
<body>
<div class="page">

  <header class="section site-header">
    <a class="abs brand" href="http://www.vel-brook.co">velbrook</a>
    <nav class="abs main-nav">
      <a href="#">Home</a><a href="#">About Us</a><a href="#">Artists</a><a href="#">Contact Us</a>
    </nav>
    <a class="abs btn header-cta" href="#">Read More</a>
  </header>

  <section class="section hero" role="img" aria-label="Woman in profile beside a tablet showing the velbrook name, with colourful paint splashes on a stone wall">
    <div class="abs hero-dots"><span></span><span></span><span></span><span></span></div>
  </section>

  <section class="section band what">
    <div class="abs shot" role="img" aria-label="Screenshot of the gallery management artwork list"></div>
    <h2 class="abs feature-title">What?</h2>
    <p class="abs feature-copy">velbrook is one of the only truly web-based gallery management software systems currently available for galleries, artists, consultants and collectors. On a basic level, it allows you to manage your artists, art inventory, clients, and invoices in one clean interface that is highly integrated. This integration allows for searchability, recordability and exportation of information, all increasing efficiency.</p>
    <a class="abs btn feature-btn" href="#">Read More</a>
  </section>

  <section class="section where">
    <h2 class="abs feature-title">Where?</h2>
    <p class="abs feature-copy">velbrook is hosted on our state-of-the art secure server that is available from anywhere via our website. To access your account, simply login through our webpage using your customized username and password. You can connect anytime/anywhere from your Nimbook, PC, phone or tablet device with a simple internet connection.</p>
    <a class="abs btn feature-btn" href="#">Read More</a>
    <div class="abs photo" role="img" aria-label="Young woman holding paintbrushes beside a hand-lettered Where? sign"></div>
  </section>

  <section class="section band why">
    <h2 class="abs feature-title">Why?</h2>
    <div class="abs art" role="img" aria-label="Blurred typewriter lettering reading Why?"></div>
    <p class="abs feature-copy">velbrook is attractive, accessible, and affordable. we have developed a system with a clean design that is easy to use, can be accessed from anywhere in the world anytime day or night, and is less expensive than any other similar product currently on the market. velbrook's sleek interface will be appreciated by your clients and artists. The simplified and pared down platform will allow you to quickly and efficiently add inventory, look up clients' past purchases, and export reports for sales. And the attractive price point is just an added bonus.</p>
    <a class="abs btn feature-btn" href="#">Read More</a>
  </section>

  <section class="section price">
    <h2 class="abs feature-title">How Much?</h2>
    <div class="abs price-body">
      <p class="feature-copy">velbrook is one of the most affordable gallery database options on the marketplace with an initial activation fee of $500 and a modest monthly maintenance fee of $99. That's it, and with that is included system set-up if using our import template, support, hosting, back-up and any upgrades to improve the system.</p>
      <p class="signup-line">Click here to <a href="#">sign-up.</a></p>
    </div>
    <div class="abs device" role="img" aria-label="Tablet showing a gallery of poster thumbnails"></div>
  </section>

  <section class="section band newsletter">
    <h2>Need help getting started?</h2>
    <p>Want assistance uploading your client list, art inventory, or past sales? Email us here.</p>
    <div class="abs email-field" aria-label="Email address"></div>
    <a class="abs subscribe" href="#">Subscribe</a>
  </section>

  <footer class="section site-footer">
    <div class="abs footer-about">
      <h3>About Us</h3>
      <p>Lorem Ipsum is simply dummy text of the printing and typesetting industry. Lorem Ipsum has been the industry's standard dummy text ever since the 1500s, when an unknown printer took a galley of type and scrambled it to make a type specimen book. It has survived not only five centuries, but also the leap into electronic typesetting, remaining essentially unchanged.</p>
    </div>
    <ul class="abs footer-links links-a">
      <li><a href="#">Home</a></li><li><a href="#">About Us</a></li><li><a href="#">Artists</a></li><li><a href="#">Contact Us</a></li>
    </ul>
    <ul class="abs footer-links links-b">
      <li><a href="#">Blog</a></li><li><a href="#">Terms and conditions</a></li><li><a href="#">Privacy policy</a></li><li><a href="#">Disclaimer</a></li><li><a href="#">Legal Notice</a></li>
    </ul>
    <ul class="abs social">
      <li>Murmurly<span></span></li>
      <li>Circlenet<span></span></li>
      <li>Workwell<span></span></li>
    </ul>
  </footer>

  <div class="section legal">©2013 Company Name , All Rights Reserved</div>

</div>
</body>
</html>
```